Eneginering consultancy brochure style web design project

Looking for a new brochure style web page for our small engineering consultancy. The prupose of the website is to provide some basic information with about the company, including exampels of our work, and present a way to initiate contact. There there will only be a few pages (up to 5) and limited content.A main focus of the project is to develop the visual design/identity for the webpage, and to provide the template for us to add content, rearrange layout and modify pages with relative ease.A mixture of text and images will be used. The use of an image slider would be desirable.We have recently had a new company logo developed (uploaded), which defines the colour scheme for the page.A professional. clean look is desired, that is not cluttered and easy to navigate.Template to add a photo slider is desirable.The use of swirl patterns (suach as those used here: https://www.brightvortexlab.co.uk/) and/or contoured mesh pattern (example attached) within the page is likely to be attractive, as this is in harmony with our activities.

Target Market(s)

Engineering; manufacturing

Industry/Entity Type

Engineering Consultant

Coding

Coded - Design and coding required

Number of Pages Required

3 page

Font styles to use
Other font styles liked:
• Helvetica

Colors
00a990
33b8a4
86cfc6
606060
3176b5
0255a3
85acd3
474747
7f7f7f

Requirements
Must have
• 1) Landing page for information about the company. Mostly text, with image slider.
• 2) One page for example projects. Images with accompanying texts.
• 3) Enquiry/'get in touch' page.
• Simple, uncluttered look and feel.

```html
<!DOCTYPE html>
<html lang="en">
<head>
<meta charset="utf-8">
<title>Northfield Thermal — Services</title>
<link href="https://fonts.googleapis.com/css2?family=Arimo:wght@400;700&family=Archivo+Black&family=Open+Sans:wght@400&display=swap" rel="stylesheet">
<style>
  :root {
    --teal: #22ae93;
    --teal-light: #5fc2ae;
    --blue-deep: #0f4aa6;
    --blue-mid: #2a64bd;
    --ink: #111111;
    --text: #1e1e1e;
    --dark: #454545;
    --white: #ffffff;
  }
  * { margin: 0; padding: 0; box-sizing: border-box; }
  html, body { width: 837px; height: 1200px; overflow: hidden; background: var(--white); }
  body { position: relative; font-family: "Arimo", Helvetica, Arial, sans-serif; color: var(--text); }

  .hero { position: absolute; left: 0; top: 0; width: 837px; height: 442px; background: var(--teal); }
  .brand { position: absolute; left: 35px; top: 30px; color: var(--white); font-weight: 700; font-size: 26px; line-height: 1; letter-spacing: 0.5px; }
  .brand-footer { left: 90px; top: 1122px; }
  .nav { position: absolute; top: 26px; right: 27px; display: flex; gap: 22px; list-style: none; }
  .nav a { color: var(--white); text-decoration: none; font-weight: 700; font-size: 10px; letter-spacing: 0.2px; display: block; padding-bottom: 4px; }
  .nav a.is-active { border-bottom: 2px solid var(--white); }
  .hero-title { position: absolute; left: 0; width: 837px; top: 172px; text-align: center; color: var(--white); font-weight: 700; font-size: 24px; line-height: 31px; letter-spacing: 0.3px; }
  .btn-contact { position: absolute; left: 346px; top: 261px; width: 145px; height: 40px; background: var(--white); color: var(--teal); font-weight: 700; font-size: 14px; display: flex; align-items: center; justify-content: center; border-radius: 2px; text-decoration: none; }

  .services-art { position: absolute; left: 0; top: 470px; }
  .mesh { position: absolute; left: 380px; top: 800px; width: 457px; height: 220px; background: radial-gradient(ellipse at 50% 50%, rgba(200,200,200,0.35), rgba(255,255,255,0) 70%); }

  .services { position: absolute; left: 475px; top: 576px; width: 320px; }
  .services-mark { width: 42px; height: 4px; background: var(--teal); margin-bottom: 20px; border-radius: 2px; }
  .services h2 { font-family: "Archivo Black", "Arimo", sans-serif; font-weight: 400; font-size: 18px; color: var(--ink); letter-spacing: 0.2px; margin-bottom: 14px; }
  .services p { font-family: "Open Sans", Arial, sans-serif; font-size: 9.5px; line-height: 13.4px; width: 280px; }
  .service-list { list-style: none; margin-top: 22px; font-family: "Open Sans", Arial, sans-serif; font-size: 9.5px; }
  .service-list li { position: relative; padding-left: 16px; height: 22px; }
  .service-list li::before { content: ""; position: absolute; left: 3px; top: 3px; border-left: 4px solid var(--blue-mid); border-top: 3.5px solid transparent; border-bottom: 3.5px solid transparent; }
  .btn-more { position: absolute; left: 2px; top: 257px; width: 96px; height: 32px; background: var(--teal); color: var(--white); font-weight: 700; font-size: 11px; display: flex; align-items: center; justify-content: center; text-decoration: none; border-radius: 1px; }

  .footer { position: absolute; left: 0; top: 1060px; width: 837px; height: 140px; }
  .copyright { position: absolute; left: 608px; top: 1154px; color: var(--white); font-size: 7.5px; }
</style>
</head>
<body>
  <header class="hero">
    <div class="brand">Northfield Thermal</div>
    <ul class="nav">
      <li><a href="#">HOME</a></li>
      <li><a href="#">ABOUT US</a></li>
      <li><a href="#" class="is-active">SERVICES</a></li>
      <li><a href="#">EXAMPLE OF WORK</a></li>
      <li><a href="#">CONTACT US</a></li>
    </ul>
    <h1 class="hero-title">SIMULATIONS AND ANALYSIS<br>OF ELECTRICAL MACHINES</h1>
    <a class="btn-contact" href="#">GET IN TOUCH</a>
  </header>

  <div class="mesh" role="img" aria-label="Soft grey dotted mesh wave pattern"></div>

  <svg class="services-art" width="430" height="530" viewBox="0 470 430 530">
    <defs>
      <linearGradient id="photoTone" x1="0" y1="0" x2="1" y2="1">
        <stop offset="0" stop-color="#3a6cc0"/>
        <stop offset="1" stop-color="#0c43a0"/>
      </linearGradient>
    </defs>
    <polygon points="194,517 413,737 194,956" fill="none" stroke="var(--teal-light)" stroke-width="6"/>
    <polygon role="img" aria-label="Photo of copper windings in an electric motor stator, tinted blue" points="143,486 394,737 143,987 -108,737" fill="url(#photoTone)"/>
  </svg>

  <section class="services">
    <div class="services-mark"></div>
    <h2>OUR SERVICES</h2>
    <p>Northfield Thermal offers thermal analysis and design for electrical machine design projects. We use a range of both commercial and in-house software for the design and optimisation of electrical machines using a multi-physics approach.</p>
    <ul class="service-list">
      <li>Experience and intuition for concept generation</li>
      <li>Thermo-fluid modelling and simulation for design development</li>
      <li>Application of a range of thermal simulation tools</li>
      <li>Test data acquisition for design validation and optimisation</li>
    </ul>
    <a class="btn-more" href="#">READ MORE</a>
  </section>

  <svg class="footer" width="837" height="140" viewBox="0 0 837 140">
    <path d="M0,12 C150,0 300,20 450,40 C600,58 760,50 837,15 L837,140 L0,140 Z" fill="var(--teal)"/>
    <path d="M0,22 C150,12 300,30 450,48 C620,66 770,60 837,22 L837,140 L0,140 Z" fill="var(--white)"/>
    <path d="M0,25 C150,16 300,34 450,52 C620,70 775,64 837,26 L837,140 L0,140 Z" fill="var(--dark)"/>
  </svg>
  <div class="brand brand-footer">Northfield Thermal</div>
  <div class="copyright">Copyrights @ 2019 All Rights Reserved</div>
</body>
</html>
```